Blue Heron IT Business Card - Clean, Simple

Need a simple, clean standard sized business card for an IT consulting business using existing logo and company colours. Background should be mainly white. Feel free to be creative but clean, simple, quiet design is preferred. Font is specified in logo but any sans serif fonts work.

Contact Information for card is as follows (doesn't need to be in this exact order):

Martin Calloway
Owner
martin@blueheronit.ca
705-391-2586
www.blueheronit.ca

Target Market(s)

Small to medium sized business.

Industry/Entity Type

IT Consulting

Contact Information for Business Card

Logo and contact info.

Font styles to use
Sans Serif

Colors
EE7325
F08F49
F5BC92
FAE3D3
FDF4ED

Requirements
Must have
• All white or mostly white background.

```html
<!DOCTYPE html>
<html lang="en">
<head>
<meta charset="utf-8">
<title>Blue Heron IT – Business Card</title>
<link rel="stylesheet" href="https://fonts.googleapis.com/css2?family=Poppins:wght@400;500;600;800&display=swap">
<style>
  :root {
    --accent: #ea531e;
    --paper: #f5f5f5;
    --ink: #141414;
    --ink-soft: #2f2f2f;
    --on-accent: #ffffff;
  }
  * { margin: 0; padding: 0; box-sizing: border-box; }
  html, body { width: 1200px; height: 687px; overflow: hidden; background: var(--paper); }
  .card {
    position: relative;
    width: 1200px;
    height: 687px;
    background: var(--paper);
    font-family: "Poppins", sans-serif;
    overflow: hidden;
  }
  .contact-panel {
    position: absolute;
    left: 0;
    top: 0;
    width: 780px;
    height: 687px;
  }
  .contact-panel .panel-fill { fill: var(--accent); }
  .contact-panel .panel-frame { fill: none; stroke: var(--accent); stroke-width: 4; }

  .contact-list {
    position: absolute;
    left: 166px;
    top: 210px;
    list-style: none;
  }
  .contact-item {
    display: flex;
    align-items: center;
    height: 48px;
    margin-bottom: 63px;
    color: var(--on-accent);
    font-size: 22px;
    font-weight: 600;
    letter-spacing: 0.1px;
  }
  .contact-icon {
    width: 40px;
    height: 40px;
    margin-right: 31px;
    flex: none;
  }
  .contact-icon circle { fill: none; stroke: var(--on-accent); stroke-width: 2.5; }
  .contact-icon .glyph { fill: var(--on-accent); }

  .brand {
    position: absolute;
    top: 60px;
    right: 124px;
    display: flex;
    flex-direction: column;
    align-items: center;
  }
  .brand-dot {
    width: 40px;
    height: 40px;
    border-radius: 50%;
    background: var(--accent);
    margin-bottom: 22px;
  }
  .brand-name {
    font-size: 28px;
    font-weight: 500;
    color: var(--ink-soft);
    letter-spacing: 0.2px;
  }

  .identity {
    position: absolute;
    right: 124px;
    top: 366px;
    text-align: right;
  }
  .identity-name {
    font-size: 52px;
    font-weight: 800;
    line-height: 49px;
    color: var(--ink);
    letter-spacing: 0.5px;
  }
  .identity-role {
    margin-top: 6px;
    font-size: 25px;
    font-weight: 400;
    color: var(--ink-soft);
  }
  .identity-rule {
    display: block;
    width: 144px;
    height: 4px;
    margin: 18px 0 0 auto;
    background: var(--accent);
  }
</style>
</head>
<body>
<div class="card">
  <svg class="contact-panel" viewBox="0 0 780 687" aria-hidden="true">
    <path class="panel-frame" d="M 50 78 L 652 78 Q 690 78 702 114 L 756 312 Q 766 347 756 382 L 702 580 Q 690 616 652 616 L 50 616 Q -16 616 -16 550 L -16 144 Q -16 78 50 78 Z"/>
    <path class="panel-fill" d="M 60 94 L 640 94 Q 672 94 684 124 L 736 318 Q 744 347 736 376 L 684 570 Q 672 600 640 600 L 60 600 Q 0 600 0 540 L 0 154 Q 0 94 60 94 Z"/>
  </svg>

  <ul class="contact-list">
    <li class="contact-item">
      <svg class="contact-icon" viewBox="0 0 40 40" aria-hidden="true">
        <circle cx="20" cy="20" r="17.5"/>
        <path class="glyph" d="M12 14h16v12H12z M13 15.5l7 5.5 7-5.5" fill="var(--on-accent)" stroke="var(--accent)" stroke-width="1.4"/>
      </svg>
      <span class="contact-text">martin@blueheronit.ca</span>
    </li>
    <li class="contact-item">
      <svg class="contact-icon" viewBox="0 0 40 40" aria-hidden="true">
        <circle cx="20" cy="20" r="17.5"/>
        <path class="glyph" d="M14.5 12.5c1-.8 2-.6 2.6.3l1.6 2.5c.5.8.3 1.6-.4 2.2l-1.1.9c.7 1.9 2.3 3.6 4.3 4.5l.9-1.1c.6-.7 1.5-.8 2.2-.3l2.5 1.6c.9.6 1 1.7.3 2.6l-1 1.2c-.8.9-2.1 1.2-3.3.8-4.7-1.6-8.3-5.2-9.8-9.9-.4-1.2-.1-2.5.8-3.3z"/>
      </svg>
      <span class="contact-text">705-391-2586</span>
    </li>
    <li class="contact-item">
      <svg class="contact-icon" viewBox="0 0 40 40" aria-hidden="true">
        <circle cx="20" cy="20" r="17.5"/>
        <path class="glyph" d="M15 12l11 9.5-5 .6 3 5.6-2 1-3-5.6-4 3.3z"/>
      </svg>
      <span class="contact-text">www.blueheronit.ca</span>
    </li>
  </ul>

  <div class="brand">
    <span class="brand-dot"></span>
    <span class="brand-name">Blue Heron IT</span>
  </div>

  <div class="identity">
    <h1 class="identity-name">Martin<br>Calloway</h1>
    <p class="identity-role">Owner</p>
    <span class="identity-rule"></span>
  </div>
</div>
</body>
</html>
```